Design Letterhead and Business Card for a travel company

Please refer to the attached document for the details to be included in the letterhead and business cards. Logo and contact details enclosed therein. Client is looking for a professional image.

Please include as many contact details as possible in your entries.

```html
<!DOCTYPE html>
<html lang="en">
<head>
<meta charset="utf-8">
<title>Swiftroute Business Card</title>
<link href="https://fonts.googleapis.com/css2?family=Lato:wght@400;700&display=swap" rel="stylesheet">
<style>
  :root {
    --backdrop: #3b3b3d;
    --paper: #ffffff;
    --brand-blue: #2a9fdc;
    --brand-purple: #5b2d86;
    --ink: #3a3a3a;
    --ink-soft: #7a7a7a;
    --rule: #b5b5b5;
  }
  * { margin: 0; padding: 0; box-sizing: border-box; }
  html, body { width: 1200px; height: 749px; overflow: hidden; }
  body {
    background: var(--backdrop);
    font-family: "Lato", sans-serif;
    position: relative;
  }
  .card {
    position: absolute;
    top: 70px;
    width: 330px;
    height: 610px;
    background: var(--paper);
    border-top: 5px solid var(--brand-blue);
    border-bottom: 9px solid var(--brand-blue);
    box-shadow: 0 8px 24px rgba(0,0,0,0.35);
  }
  .card--front { left: 245px; }
  .card--back { left: 625px; }

  .brand {
    position: absolute;
    left: 0; right: 0;
    display: flex;
    align-items: center;
    justify-content: center;
    gap: 10px;
  }
  .card--front .brand { top: 150px; }
  .card--back .brand { top: 270px; }
  .brand__dot {
    width: 18px; height: 18px;
    border-radius: 50%;
    background: var(--brand-purple);
  }
  .brand__name {
    font-weight: 700;
    font-size: 34px;
    letter-spacing: 1px;
    color: var(--brand-blue);
  }

  .holder {
    position: absolute;
    top: 320px; left: 0; right: 0;
    text-align: center;
  }
  .holder__name {
    font-size: 23px;
    font-weight: 700;
    letter-spacing: 0.5px;
    color: var(--brand-blue);
  }
  .holder__name span { color: var(--ink-soft); }
  .holder__title {
    font-size: 14px;
    color: var(--ink);
    margin-top: 2px;
  }

  .contacts {
    position: absolute;
    top: 382px; left: 40px; right: 40px;
    border-top: 1px solid var(--rule);
    border-bottom: 1px solid var(--rule);
    padding: 20px 0 22px 38px;
    list-style: none;
  }
  .contacts__item {
    display: flex;
    align-items: center;
    gap: 16px;
    font-size: 13px;
    color: var(--ink);
    height: 26px;
  }
  .contacts__icon { width: 15px; height: 15px; fill: var(--ink); }

  .site {
    position: absolute;
    bottom: 36px; left: 0; right: 0;
    display: flex;
    justify-content: center;
    align-items: center;
    gap: 10px;
    font-size: 14px;
    color: var(--ink);
  }
  .site__icon { width: 17px; height: 17px; }
</style>
</head>
<body>
  <section class="card card--front">
    <div class="brand">
      <span class="brand__dot"></span>
      <span class="brand__name">SWIFTROUTE</span>
    </div>

    <div class="holder">
      <h1 class="holder__name">TALIA <span>MOKOENA</span></h1>
      <p class="holder__title">Director / Owner</p>
    </div>

    <ul class="contacts">
      <li class="contacts__item">
        <svg class="contacts__icon" viewBox="0 0 16 16"><path d="M1 5c0-2 3-3 7-3s7 1 7 3v1h-3.5V4.5h-7V6H1zM4 7h8l2 7H2z"/></svg>
        071 555 03218
      </li>
      <li class="contacts__item">
        <svg class="contacts__icon" viewBox="0 0 16 16"><path d="M1 3h14v10H1zM2.2 4.2v.5L8 9l5.8-4.3v-.5zM2.2 6.2v5.6h11.6V6.2L8 10.5z"/></svg>
        info@swiftroute.co.za
      </li>
      <li class="contacts__item">
        <svg class="contacts__icon" viewBox="0 0 16 16"><circle cx="8" cy="8" r="7"/><path d="M1.5 8h13M8 1c-3 3-3 11 0 14M8 1c3 3 3 11 0 14" stroke="#fff" stroke-width="1" fill="none"/></svg>
        www.swiftroute.co.za
      </li>
    </ul>
  </section>

  <section class="card card--back">
    <div class="brand">
      <span class="brand__dot"></span>
      <span class="brand__name">SWIFTROUTE</span>
    </div>

    <div class="site">
      <svg class="site__icon" viewBox="0 0 18 18"><circle cx="9" cy="9" r="8" fill="none" stroke="#3a3a3a" stroke-width="1.4"/><path d="M6 5l7 4-7 4 1.5-4z" fill="#3a3a3a"/></svg>
      www.swiftroute.co.za
    </div>
  </section>
</body>
</html>
```